" Sou uma médica cirurgiã plástica que atendendo numa clínica (que não é própria), fazendo parte de uma equipe de cirurgiões plásticos mais experientes que atende pacientes classe A em São Paulo. Faço todos os tipos de cirurgia plástica, mas tenho uma maior foco nas cirurgias de face (bleroplastia, ritidoplastia), mamoplastia e transplante capilar, além de procedimentos (laser, preenchedores/harmonização facial, dravix). "

```html
<!DOCTYPE html>
<html lang="pt-BR">
<head>
<meta charset="utf-8">
<title>Dra. Marina Solano — Capa</title>
<link rel="stylesheet" href="https://fonts.googleapis.com/css2?family=Cinzel:wght@400&family=Montserrat:wght@400;500&display=swap">
<style>
  :root {
    --page-bg: #eef0f2;
    --rose: #d98aab;
    --plum: #9b1c63;
    --ink-light: #ffffff;
    --watermark: rgba(190, 60, 130, 0.35);
    --photo-mauve: #a8899f;
    --photo-skin: #e2c3b4;
    --photo-skin-deep: #cfa593;
    --photo-glove: #f3f4f7;
    --photo-coat: #dde2ea;
  }
  * { margin: 0; padding: 0; box-sizing: border-box; }
  html, body { width: 1200px; height: 1200px; overflow: hidden; background: var(--page-bg); }
  .canvas { position: relative; width: 1200px; height: 1200px; }
  .cover {
    position: absolute; left: 40px; top: 387px;
    width: 1120px; height: 426px; overflow: hidden;
    box-shadow: 0 4px 18px rgba(0,0,0,.12);
  }
  .cover-photo {
    position: absolute; inset: 0;
    background:
      radial-gradient(ellipse 240px 300px at 430px 250px, var(--photo-skin) 0%, var(--photo-skin-deep) 55%, rgba(207,165,147,0) 100%),
      radial-gradient(ellipse 260px 120px at 560px 70px, var(--photo-glove) 0%, rgba(243,244,247,0) 100%),
      linear-gradient(90deg, var(--photo-mauve) 0%, #b99aac 20%, #d6c2c4 45%, var(--photo-coat) 70%, #eef0f4 100%);
  }
  .watermark {
    position: absolute; left: 40px; top: 22px; width: 340px; height: 300px;
    pointer-events: none;
  }
  .watermark-square {
    position: absolute; left: 60px; top: 0; width: 220px; height: 220px;
    border: 14px solid var(--watermark);
  }
  .watermark-name {
    position: absolute; left: 0; top: 240px; width: 340px; text-align: center;
    font-family: 'Cinzel', serif; font-size: 36px; color: var(--watermark);
    white-space: nowrap;
  }
  .cover-shapes { position: absolute; inset: 0; }
  .brand {
    position: absolute; left: 840px; top: 70px; width: 280px;
    text-align: center; color: var(--ink-light);
  }
  .brand-mark {
    width: 34px; height: 34px; margin: 0 auto 14px;
    border: 2px solid var(--ink-light);
  }
  .brand-title {
    font-family: 'Montserrat', sans-serif; font-size: 11px; letter-spacing: 2px;
    text-transform: uppercase; text-align: left; padding-left: 36px;
  }
  .brand-name {
    font-family: 'Cinzel', serif; font-size: 30px; font-weight: 400;
    line-height: 1; letter-spacing: 1px;
  }
  .brand-specialty {
    font-family: 'Montserrat', sans-serif; font-size: 10px; letter-spacing: 3px;
    text-transform: uppercase; margin-top: 6px;
  }
  .contacts {
    position: absolute; left: 880px; top: 318px;
    list-style: none; color: var(--ink-light);
    font-family: 'Montserrat', sans-serif; font-size: 12px; line-height: 1.25;
  }
  .contacts li { display: flex; align-items: flex-start; gap: 10px; margin-bottom: 7px; }
  .contacts svg { flex: none; width: 13px; height: 13px; margin-top: 1px; }
</style>
</head>
<body>
<main class="canvas">
  <section class="cover">
    <div class="cover-photo" role="img" aria-label="Fotografia de paciente recebendo avaliação facial com mãos de médica em luvas brancas"></div>
    <div class="watermark" aria-hidden="true">
      <div class="watermark-square"></div>
      <p class="watermark-name">Marina Solano</p>
    </div>
    <svg class="cover-shapes" viewBox="0 0 1120 426" width="1120" height="426" aria-hidden="true">
      <rect x="840" y="0" width="280" height="426" fill="var(--rose)"/>
      <polygon points="386,426 1120,205 1120,426" fill="var(--plum)"/>
    </svg>
    <div class="brand">
      <div class="brand-mark"></div>
      <p class="brand-title">Dra.</p>
      <p class="brand-name">Marina Solano</p>
      <p class="brand-specialty">Cirurgia Plástica</p>
    </div>
    <ul class="contacts">
      <li>
        <svg viewBox="0 0 24 24"><path fill="#fff" d="M6.6 10.8a15 15 0 0 0 6.6 6.6l2.2-2.2a1 1 0 0 1 1-.25 11.4 11.4 0 0 0 3.6.57 1 1 0 0 1 1 1V20a1 1 0 0 1-1 1A17 17 0 0 1 3 4a1 1 0 0 1 1-1h3.5a1 1 0 0 1 1 1c0 1.250.2 2.450.57 3.57a1 1 0 0 1-.25 1z"/></svg>
        <span>(11) 5400-2718</span>
      </li>
      <li>
        <svg viewBox="0 0 24 24"><circle cx="12" cy="12" r="9" fill="none" stroke="#fff" stroke-width="2.4"/></svg>
        <span>(11) 98841-207</span>
      </li>
      <li>
        <svg viewBox="0 0 24 24"><path fill="#fff" d="M12 2a7 7 0 0 0-7 7c0 5.2 7 13 7 13s7-7.8 7-13a7 7 0 0 0-7-7zm0 9.5A2.5 2.5 0 1 1 12 6.5a2.5 2.5 0 0 1 0 5z"/></svg>
        <span>R. das Acácias, nº 420<br>Jardins - São Paulo</span>
      </li>
    </ul>
  </section>
</main>
</body>
</html>
```